Hollow Birch Vintners Reserve Cabernet Sauvignon Wine Labels front and back

I need a front and back wine label. For a new RESERVE Cabernet Sauvignon wine. I am attaching the details and some ideas and possible images to use. But creativity is encouraged. This wine will be seen on wine shop and grocery store shelves so it needs to pop while appearing elegant and to be about $50/bottle of wine. The front and back labels should go together nicely. I would like some foil on the front, but not the back. We are trying to show the natural beauty of our vineyards and the elegance of our wines. We would like to invoke a feel of sustainability, proudly family owned and operated.

Target Market(s)

21-50 year olds, red wine drinkers, higher priced wine drinkers

Industry/Entity Type

Wine

Font styles to use
Serif
Script

Colors

Designer to choose only greyscale colors for use in the design.

Requirements
Must have
• Front Label with specified details and Back label with specified details. Foil banner on the front label that says " Family stewards of the land for 5 generations"the front label that says
Nice to have
• vineyard or winery background, have include a sample or example, some gold or bronze or silver accents

```html
<!DOCTYPE html>
<html lang="en">
<head>
<meta charset="UTF-8">
<title>Hollow Birch Vintners – Reserve Cabernet Sauvignon Labels</title>
<link href="https://fonts.googleapis.com/css2?family=Cinzel:wght@600;700&family=Cormorant+Garamond:ital,wght@0,500;0,600;0,700;1,500&family=Pinyon+Script&display=swap" rel="stylesheet">
<style>
  :root {
    --backdrop: #1d1d1f;
    --front-stone: #8c847b;
    --front-stone-dark: #6f675f;
    --ink: #2a2520;
    --gold: #d9b45a;
    --gold-light: #f3dc8e;
    --gold-deep: #a9822f;
    --back-umber: #3a3029;
    --back-umber-dark: #2c241f;
    --cream: #ece3d2;
    --art-dark: #4f4841;
    --art-light: #a39a8f;
  }
  * { box-sizing: border-box; margin: 0; padding: 0; }
  html, body { width: 1200px; height: 926px; overflow: hidden; }
  body { background: var(--backdrop); position: relative; font-family: "Cormorant Garamond", serif; }

  /* Front label */
  .front-label {
    position: absolute; left: 110px; top: 88px; width: 440px; height: 750px;
    background: linear-gradient(180deg, var(--front-stone) 0%, var(--front-stone-dark) 100%);
    text-align: center; color: var(--ink);
  }
  .grape-art {
    position: absolute; left: 110px; top: 14px; width: 220px; height: 120px;
    background: radial-gradient(ellipse at 50% 45%, var(--art-dark) 0%, rgba(79,72,65,0.35) 60%, transparent 75%);
  }
  .front-brand {
    position: absolute; top: 150px; left: 0; right: 0;
    font-family: "Cinzel", serif; font-weight: 700; font-size: 40px; line-height: 1.15;
    letter-spacing: 1px; color: var(--gold);
  }
  .front-reserve {
    position: absolute; top: 270px; left: 0; right: 0;
    font-weight: 700; font-size: 17px; letter-spacing: 1px;
  }
  .front-varietal {
    position: absolute; top: 290px; left: 0; right: 0;
    font-weight: 600; font-size: 30px; letter-spacing: 0.5px; color: var(--gold);
  }
  .front-region {
    position: absolute; top: 326px; left: 0; right: 0;
    font-family: "Pinyon Script", cursive; font-size: 34px; color: var(--gold);
  }
  .vineyard-art {
    position: absolute; left: 24px; top: 378px; width: 392px; height: 260px;
    background: linear-gradient(180deg, var(--art-light) 0%, var(--art-dark) 55%, var(--front-stone-dark) 100%);
    opacity: 0.75;
  }
  .front-vintage {
    position: absolute; top: 650px; left: 0; right: 0;
    font-weight: 600; font-size: 30px; letter-spacing: 1px;
  }
  .foil-banner {
    position: absolute; left: 0; right: 0; bottom: 18px; height: 30px;
    background: linear-gradient(90deg, var(--gold-deep), var(--gold-light) 45%, var(--gold) 70%, var(--gold-deep));
    font-weight: 700; font-size: 13px; letter-spacing: 0.6px; line-height: 30px; color: var(--ink);
  }

  /* Back label */
  .back-label {
    position: absolute; left: 620px; top: 93px; width: 470px; height: 740px;
    background: linear-gradient(180deg, var(--back-umber) 0%, var(--back-umber-dark) 100%);
    color: var(--cream);
  }
  .back-frame { position: absolute; inset: 14px; border: 1.5px solid var(--gold); }
  .back-frame-inner { position: absolute; inset: 22px; border: 0.75px solid rgba(217,180,90,0.55); }
  .back-brand {
    position: absolute; top: 62px; left: 0; right: 0; text-align: center;
    font-family: "Cinzel", serif; font-weight: 600; font-size: 25px; letter-spacing: 1px; color: var(--gold);
  }
  .back-rule { position: absolute; top: 100px; left: 150px; width: 170px; height: 1px; background: var(--gold); }
  .back-story {
    position: absolute; top: 130px; left: 48px; right: 48px; text-align: center;
    font-size: 16px; line-height: 1.5; font-weight: 500;
  }
  .back-signoff {
    position: absolute; top: 345px; left: 0; right: 0; text-align: center;
    font-style: italic; font-size: 12.5px; color: var(--gold);
  }
  .back-warning {
    position: absolute; top: 390px; left: 48px; right: 48px;
    font-size: 15px; line-height: 1.45; font-weight: 500;
  }
  .back-warning strong { font-weight: 700; }
  .back-legal {
    position: absolute; top: 605px; left: 48px; width: 260px;
    font-size: 10px; line-height: 1.45; font-weight: 600; letter-spacing: 0.3px;
  }
</style>
</head>
<body>
  <section class="front-label">
    <div class="grape-art" role="img" aria-label="Engraved grape cluster with vine leaves"></div>
    <h1 class="front-brand">HOLLOW BIRCH<br>VINTNERS</h1>
    <p class="front-reserve">RESERVE</p>
    <p class="front-varietal">CABERNET SAUVIGNON</p>
    <p class="front-region">Silver Ridge Hills</p>
    <div class="vineyard-art" role="img" aria-label="Engraved vineyard rows leading to a hillside winery"></div>
    <p class="front-vintage">2022</p>
    <p class="foil-banner">FAMILY STEWARDS OF THE LAND FOR 5 GENERATIONS</p>
  </section>

  <section class="back-label">
    <div class="back-frame"></div>
    <div class="back-frame-inner"></div>
    <h2 class="back-brand">HOLLOW BIRCH VINTNERS</h2>
    <div class="back-rule"></div>
    <p class="back-story">“Our vineyards, nestled along the Columbia River in Washington state, flourish in a region celebrated for its long, hot days and cool, crisp nights. This area, rich in natural resources and fertile soils, imparts a unique essence of balance, structure, and elegance to our wines.”</p>
    <p class="back-signoff">Cheers, Maren Holt &nbsp;|&nbsp; Maren Holt, Winemaker</p>
    <p class="back-warning"><strong>GOVERNMENT WARNING:</strong> (1) According to the Surgeon General, women should not drink alcoholic beverages during pregnancy because of the risk of birth defects. (2) Consumption of alcoholic beverages impairs your ability to drive a car or operate machinery, and may cause health problems.</p>
    <p class="back-legal">750 ML &nbsp;|&nbsp; CONTAINS SULFITES<br>14% ALC. BY VOL.<br>PRODUCED AND BOTTLED BY<br>LARKFIELD WINE ESTATES, LLC, ALDER FALLS WA, USA</p>
  </section>
</body>
</html>
```